Wine label refresh

We are wanting to modify our Corran Hollow label to include a picture on it.
I have attached the pictures below which we would like on the label. They are of the Corran Hollow vineyard. I have also attached an example of another label with a picture on it that we like the style of.
Updates
Industry/Entity Type
Vineyard
Requirements
Must have
- The Corran Hollow text must stay the same but can be moved down. It still needs to be the same size though.
Marlborough Sauvignon Blanc should remain in the same font and roughly the same size.
Wine of New Zealand also must stay but could potentially be moved.
Nice to have
- It would be nice if we could keep the PM logo on the front label but feel free to experiment with where this goes.

```html
<!DOCTYPE html>
<html lang="en">
<head>
<meta charset="utf-8">
<title>Corran Hollow – Marlborough Sauvignon Blanc Label</title>
<link rel="stylesheet" href="https://fonts.googleapis.com/css2?family=Cormorant+Garamond:wght@500&family=Pinyon+Script&family=Josefin+Sans:wght@300&display=swap">
<style>
  :root {
    --paper: #ffffff;
    --edge: #111111;
    --trim-cyan: #1fe3ec;
    --gold: #d68b0c;
    --ink: #111111;
    --wine-red: #cc1f2f;
    --grey: #a5a7aa;
    --monogram: #ededed;
    --photo-light: #e9e2c8;
    --photo-mid: #a89e72;
    --photo-dark: #4a4526;
  }
  * { margin: 0; padding: 0; box-sizing: border-box; }
  html, body { width: 1200px; height: 1001px; overflow: hidden; background: var(--paper); }
  .label {
    position: relative;
    width: 1200px;
    height: 1001px;
    background: var(--paper);
    border: 1px solid var(--edge);
    overflow: hidden;
  }
  .frame { position: absolute; }
  .frame--cut {
    left: 23px; top: 71px; width: 1158px; height: 862px;
    border: 2px solid var(--trim-cyan); border-radius: 6px;
  }
  .frame--outer-rule {
    left: 47px; top: 100px; width: 1111px; height: 804px;
    border: 2px solid var(--gold);
  }
  .frame--band {
    left: 70px; top: 126px; width: 1064px; height: 755px;
    border: 32px solid var(--gold);
  }
  .frame--inner-rule {
    left: 114px; top: 170px; width: 975px; height: 667px;
    border: 2px solid var(--gold);
  }
  .vineyard-photo {
    position: absolute;
    left: 278px; top: 197px; width: 649px; height: 272px;
    border: 1px solid var(--gold);
    background:
      linear-gradient(180deg, var(--photo-light) 0%, var(--photo-mid) 35%, var(--photo-dark) 60%, var(--photo-mid) 100%);
  }
  .monogram {
    position: absolute;
    left: 0; width: 100%; top: 455px;
    text-align: center;
    font-family: "Cormorant Garamond", serif;
    font-weight: 500;
    font-size: 280px;
    line-height: 1;
    color: var(--monogram);
    padding-left: 30px;
  }
  .estate-name {
    position: absolute;
    left: 0; width: 100%; top: 498px;
    text-align: center;
    font-family: "Cormorant Garamond", serif;
    font-weight: 500;
    font-size: 84px;
    line-height: 1;
    font-variant: small-caps;
    letter-spacing: 5px;
    color: var(--ink);
  }
  .varietal, .vintage {
    position: absolute;
    left: 0; width: 100%;
    text-align: center;
    font-family: "Pinyon Script", cursive;
    color: var(--wine-red);
    line-height: 1;
  }
  .varietal { top: 630px; font-size: 58px; }
  .vintage { top: 705px; font-size: 52px; padding-left: 10px; }
  .details {
    position: absolute;
    left: 130px; right: 128px; top: 786px;
    display: flex; justify-content: space-between;
    font-family: "Josefin Sans", sans-serif;
    font-weight: 300;
    font-size: 35px;
    line-height: 1;
    color: var(--grey);
  }
</style>
</head>
<body>
  <main class="label">
    <div class="frame frame--cut"></div>
    <div class="frame frame--outer-rule"></div>
    <div class="frame frame--band"></div>
    <div class="frame frame--inner-rule"></div>

    <div class="vineyard-photo" role="img" aria-label="Sepia photograph of the vineyard rows with a farmhouse, tall palm trees and hills behind"></div>

    <div class="monogram" aria-hidden="true">PM</div>

    <h1 class="estate-name">Corran Hollow</h1>
    <p class="varietal">Marlborough Sauvignon Blanc</p>
    <p class="vintage">2012</p>

    <div class="details">
      <span class="details__volume">750ml</span>
      <span class="details__origin">NEW ZEALAND WINE</span>
      <span class="details__abv">13% alc/vol</span>
    </div>
  </main>
</body>
</html>
```